CREW VORTEX Martials Arts Gym - DL Flyer Design to launch their new location!!

We need a 1 sided DL flyer design (in landscape) for a martial arts gym with a world class facility specialising in Kickboxing, Muay Thai, MMA, Boxing, Ladies Classes and Kids Classes. More info may be obtained at www.vortexharlow.com.au

The design should communicate who we are / what we do

This flyer will be distributed to 10,000 houses within a 10km radius of the gym

Target Market(s)

*Our target market is males aged 20 - 30 who are looking for a challenging training regime (sick and tired of the boring old treadmill)

*Should also be family friendly for mothers and kids wishing to join our gym

Industry/Entity Type

Gym

Requirements
Must have
• *Flyer must demonstrate who we are / what we do (gaining awareness, these flyers will be distributed to 10,000 homes within a 10km radius)
• *Must include an incentive coupon offer - FREE CLASS PASS or something of the likes.
• *Must include our partner logos Korvane / Brimlock / Global Striking Federation / Kickfight Oceania and GPLB (all logos have been provided)
• *Web address / Address / Contact number / Linkspot Icon
• W: www.vortexharlow.com.au
• A: 42 Marlow Road, Harlow VIC 3091
• C: (03) 9572 6180
• *Images have been provided of the gym and some of our members during classes (more information may be gained at our website www.vortexharlow.com.au)
Nice to have
• *Colours preferred but NOT essential are splashes of blue & red combination (boxing ring corner colours)

```html
<!DOCTYPE html>
<html lang="en">
<head>
<meta charset="utf-8">
<title>Crew Vortex Gym – DL Flyer</title>
<link href="https://fonts.googleapis.com/css2?family=Oswald:wght@700&family=Open+Sans:wght@300;400;700&display=swap" rel="stylesheet">
<style>
  :root{
    --blue:#1f6fc1;
    --blue-deep:#0d3d78;
    --red:#b3282d;
    --red-deep:#6e1216;
    --night:#0b0d12;
    --steel:#1c1f26;
    --gold:#b89a5a;
    --white:#ffffff;
    --ice:#dce8f5;
  }
  *{margin:0;padding:0;box-sizing:border-box}
  html,body{width:1200px;height:849px;overflow:hidden;background:var(--night)}
  .flyer{position:relative;width:1200px;height:849px;overflow:hidden;font-family:"Open Sans",Arial,sans-serif;color:var(--white);background:var(--night)}

  /* top discipline strip */
  .discipline{position:absolute;top:0;height:190px}
  .discipline--kick{left:0;width:400px;background:linear-gradient(160deg,#2a2c35,#0e0f14 60%,#3a1a1e)}
  .discipline--box{left:400px;width:440px;background:linear-gradient(180deg,#1a1c26,#3a4b8c 50%,#8a2228)}
  .discipline--mma{left:840px;width:360px;background:linear-gradient(200deg,#2b2d33,#111318 60%,#5a1d22)}
  .discipline-label{position:absolute;top:142px;font-weight:400;font-size:34px;letter-spacing:.5px;color:#f7dfe2;text-shadow:0 0 2px var(--red),0 0 6px var(--red-deep)}
  .discipline-label--kick{left:150px}
  .discipline-label--box{left:520px;color:#e6eefc;text-shadow:0 0 2px var(--blue),0 0 6px var(--blue-deep)}
  .discipline-label--mma{left:850px}

  /* gym backdrop */
  .backdrop{position:absolute;top:190px;left:0;width:1200px;height:450px;background:linear-gradient(90deg,#0f3560 0%,#1b2740 45%,#3a1d22 60%,#7c1d22 100%)}

  /* title band */
  .title-band{position:absolute;top:182px;left:0;width:1200px;height:114px;background:rgba(31,111,193,.88)}
  .title{position:absolute;top:186px;left:0;width:1200px;text-align:center;font-family:"Oswald",Impact,sans-serif;font-weight:700;font-size:96px;line-height:104px;letter-spacing:2px;color:var(--white)}
  .tagline{position:absolute;top:287px;left:0;width:1200px;text-align:center;font-weight:700;font-size:19px;letter-spacing:1px}

  /* side info panels */
  .panel{position:absolute;top:340px;height:260px;padding:30px 30px}
  .panel--facilities{left:0;width:380px;background:rgba(31,111,193,.75)}
  .panel--training{right:0;width:420px;background:rgba(179,40,45,.75);text-align:right;padding-right:24px}
  .panel h2{font-weight:400;font-size:20px;letter-spacing:.5px;margin-bottom:6px}
  .panel ul{list-style:none}
  .panel li{font-weight:300;font-size:16px;line-height:26px;color:var(--ice);padding-left:6px}

  /* free class coupon */
  .coupon{position:absolute;left:22px;top:604px;width:380px;height:32px;border:2px dashed var(--white);display:flex;align-items:center;justify-content:center;gap:10px;font-size:14px;font-weight:400;letter-spacing:.5px;background:var(--red)}
  .coupon strong{font-weight:700;font-size:16px}

  /* class photos */
  .class-photo{position:absolute;border:3px solid var(--blue)}
  .class-photo--female{left:367px;top:312px;width:250px;height:178px;background:linear-gradient(135deg,#d9d4d0,#b8a7a0 50%,#3b3134)}
  .class-photo--kids{left:619px;top:312px;width:218px;height:178px;border-color:var(--red);background:linear-gradient(135deg,#e8e3e0,#b33338 60%,#3a5aa8)}
  .class-photo--hall{left:425px;top:488px;width:342px;height:178px;background:linear-gradient(180deg,#c7c9cf,#3b4e8c 50%,#c4403d)}
  .class-caption{position:absolute;bottom:10px;left:0;width:100%;text-align:center;font-weight:700;font-size:15px;text-shadow:0 1px 3px #000}

  /* partner bar */
  .partners{position:absolute;top:640px;left:0;width:1200px;height:122px;background:linear-gradient(180deg,var(--steel),#0c0e13)}
  .partner{position:absolute;top:0;height:122px;font-weight:700;font-size:20px;line-height:22px;color:var(--white);display:flex;align-items:center;gap:8px}
  .partner--korvane{left:50px}
  .partner--kickfight{left:200px}
  .partner--striking{left:715px}
  .partner--brimlock{left:900px}
  .partner--gplb{left:1060px}
  .partner-dot{width:14px;height:14px;border-radius:50%;background:var(--red);flex:none}
  .club-mark{position:absolute;left:520px;top:630px;width:160px;height:160px;border-radius:50%;background:var(--night);border:4px solid var(--gold);display:flex;align-items:center;justify-content:center;text-align:center;font-weight:700;font-size:24px;line-height:28px;color:var(--white)}

  /* contact bar */
  .contact{position:absolute;top:762px;left:0;width:1200px;height:87px;background:linear-gradient(90deg,#7e2327,#a2363a 50%,#7e2327)}
  .address{position:absolute;left:38px;top:16px;font-weight:400;font-size:19px;line-height:25px}
  .social{position:absolute;left:0;width:1200px;top:32px;display:flex;justify-content:center;align-items:center;gap:6px;font-size:13px;font-weight:400;padding-left:400px;visibility:hidden}
  .web{position:absolute;left:390px;width:420px;top:40px;text-align:center;font-weight:300;font-size:26px;letter-spacing:1px}
  .follow{position:absolute;left:700px;top:14px;display:flex;align-items:center;gap:6px;font-size:14px;font-weight:400}
  .follow-square{width:14px;height:14px;background:var(--white)}
  .phones{position:absolute;right:22px;top:14px;font-weight:400;font-size:23px;line-height:29px;text-align:left}
</style>
</head>
<body>
<main class="flyer">
  <div class="discipline discipline--kick" role="img" aria-label="Kickboxing bout in a lit ring"></div>
  <div class="discipline discipline--box" role="img" aria-label="Amateur boxers in blue and red headgear exchanging punches"></div>
  <div class="discipline discipline--mma" role="img" aria-label="MMA fighters grappling in a cage"></div>
  <span class="discipline-label discipline-label--kick">KICKBOXING</span>
  <span class="discipline-label discipline-label--box">BOXING</span>
  <span class="discipline-label discipline-label--mma">MMA</span>

  <div class="backdrop" role="img" aria-label="Gym interior with hanging punching bags"></div>

  <div class="title-band"></div>
  <h1 class="title">CREW VORTEX GYM</h1>
  <p class="tagline">A BOXING GYM WITHOUT THE ATTITUDE.</p>

  <section class="panel panel--facilities">
    <h2>TRAINING FACILITIES</h2>
    <ul>
      <li>COMPETITION SIZE BOXING RING</li>
      <li>MATTED TRAINING AREA APPROX 250M2</li>
      <li>FULLY EQUIPPED WEIGHTS AREA</li>
      <li>CARDIO EQUIPMENT</li>
      <li>PUNCHING BAGS</li>
      <li>FLOOR TO CEILING BALLS</li>
      <li>SPEED BALLS</li>
    </ul>
  </section>

  <section class="panel panel--training">
    <h2>TRAINING OFFERED</h2>
    <ul>
      <li>BOXING, KICKBOXING &amp;</li>
      <li>MUAY THAI CLASSES</li>
      <li>FITNESS/CIRCUIT TRAINING CLASSES</li>
      <li>SPARRING SESSIONS</li>
      <li>FEMALE ONLY CLASSES</li>
      <li>KIDS ONLY CLASSES</li>
      <li>PERSONAL TRAINING (ONE-ON-ONE &amp; GROUP)</li>
    </ul>
  </section>

  <aside class="coupon"><strong>FREE CLASS PASS</strong><span>PRESENT THIS FLYER</span></aside>

  <figure class="class-photo class-photo--female" role="img" aria-label="Women training on punching bags">
    <figcaption class="class-caption">FEMALE ONLY CLASSES</figcaption>
  </figure>
  <figure class="class-photo class-photo--kids" role="img" aria-label="Children practising kicks and guard stance">
    <figcaption class="class-caption">KIDS CLASSES</figcaption>
  </figure>
  <div class="class-photo class-photo--hall" role="img" aria-label="Boxing ring and matted training floor with bags"></div>

  <section class="partners">
    <span class="partner partner--korvane">Korvane</span>
    <span class="partner partner--kickfight"><i class="partner-dot"></i>Kickfight<br>Oceania</span>
    <span class="partner partner--striking"><i class="partner-dot"></i>Global Striking<br>Federation</span>
    <span class="partner partner--brimlock">Brimlock</span>
    <span class="partner partner--gplb"><i class="partner-dot"></i>GPLB</span>
  </section>
  <div class="club-mark">CREW<br>VORTEX</div>

  <footer class="contact">
    <p class="address">42 MARLOW ROAD (ENTER VIA LINDEN ST)<br>HARLOW, VIC 3091</p>
    <p class="follow"><i class="follow-square"></i>Linkspot /vortexharlow</p>
    <p class="web">WWW.VORTEXHARLOW.COM.AU</p>
    <p class="phones">TEL: (03) 9572 6180<br>MOB: 0412 587 904</p>
  </footer>
</main>
</body>
</html>
```